Design an Outstanding flyer for my company.

I need a flyer designed for our window tinting company based in Brisbane Queensland Australia. The flyer will be targeting Home tinting. We also do mobile car tinting. Something in regards to this could be incorporated into the flyer as well.
I want it to be 2 sided DL size. Black background.
It really needs to Pop, and be a real attention getter.
It needs to be easy to read.
I have provided a mock up with the info on it from our marketing company. It will need a spellcheck etc to make sure everything is correct.
Everything about it can be changed however you like.
I have also included the company logo.

Lets see what you've got!

Target Market(s)

Home Owners

Industry/Entity Type

Home Improvement

Font styles to use
Other font styles liked:
• Duan Penh

Requirements
Must have
• All the information on the mock up. Clear and easy to read.
• Must Stand Out!

```html
<!DOCTYPE html>
<html lang="en">
<head>
<meta charset="utf-8">
<title>Brightline Window Tinting – DL Flyer</title>
<link href="https://fonts.googleapis.com/css2?family=Cinzel:wght@400;600;700&family=EB+Garamond:wght@400;700&display=swap" rel="stylesheet">
<style>
  :root{
    --stage:#546767;
    --ink:#0d0d0f;
    --panel:#141416;
    --gold:#f2cd1a;
    --gold-deep:#c99a0a;
    --gold-text:#e9c43a;
    --white:#ffffff;
    --photo-a:#d9b08c;
    --photo-b:#3f6f9c;
    --photo-c:#9fc3d8;
    --photo-d:#6f8f4e;
  }
  *{box-sizing:border-box;margin:0;padding:0}
  html,body{width:1200px;height:960px;overflow:hidden;background:var(--stage)}
  .stage{position:relative;width:1200px;height:960px}
  .flyer{
    position:absolute;top:48px;width:405px;height:834px;
    background:linear-gradient(180deg,#1a1a1c 0%,var(--ink) 60%,#1b1b1d 100%);
    overflow:hidden;color:var(--white);font-family:"Cinzel",serif;
  }
  .flyer--front{left:162px}
  .flyer--back{left:630px;top:50px}
  .hero{position:absolute;left:0;top:0;width:405px;height:262px}
  .brand{
    position:absolute;width:136px;height:156px;border-radius:50%;
    background:#050505;display:flex;align-items:center;justify-content:center;
  }
  .flyer--front .brand{left:236px;top:94px}
  .flyer--back .brand{left:234px;top:40px}
  .brand__name{
    font-family:"Cinzel",serif;font-weight:600;font-size:13px;color:var(--gold-text);
    text-align:center;line-height:1.25;letter-spacing:.5px;
  }
  .headline{position:absolute;left:0;width:100%;text-align:center;line-height:1}
  .headline--gold{top:270px;font-size:35px;color:var(--gold-text);font-weight:400;letter-spacing:.5px}
  .headline--white{top:313px;font-size:29px;font-weight:400}
  .flyer--back .headline--gold{top:262px}
  .flyer--back .headline--white{top:305px}
  .ribbon{position:absolute;left:40px;top:344px;width:336px;height:72px}
  .flyer--back .ribbon{top:336px}
  .ribbon svg{position:absolute;inset:0}
  .ribbon__text{
    position:absolute;inset:0;display:flex;align-items:center;justify-content:center;
    font-size:42px;font-weight:700;color:var(--ink);letter-spacing:.5px;
  }
  .headline--privacy{top:420px;font-size:29px;font-weight:400}
  .flyer--back .headline--privacy{top:412px}
  .benefits{
    position:absolute;left:30px;right:26px;top:460px;text-align:center;
    font-size:9.4px;line-height:16.4px;letter-spacing:.2px;
  }
  .flyer--back .benefits{top:452px}
  .reasons{
    position:absolute;left:0;right:0;top:598px;height:66px;
    background:linear-gradient(90deg,var(--gold-deep) 0%,var(--gold) 25%,#f8e04a 55%,var(--gold) 80%,var(--gold-deep) 100%);
    color:var(--ink);text-align:center;font-weight:600;font-size:13px;line-height:22.5px;padding-top:0;
  }
  .flyer--back .reasons{top:588px;height:68px}
  .cta{position:absolute;left:0;right:0;top:686px;height:60px}
  .flyer--back .cta{top:680px}
  .cta__text{
    position:absolute;left:22px;width:260px;top:6px;text-align:center;
    font-size:13.5px;line-height:23px;letter-spacing:.5px;
  }
  .cta__icon{
    position:absolute;left:289px;top:-6px;width:70px;height:70px;border-radius:50%;
    background:radial-gradient(circle at 40% 35%,#fbe65a,var(--gold) 55%,var(--gold-deep));
    display:flex;align-items:center;justify-content:center;
  }
  .contact-bar{
    position:absolute;left:0;right:0;top:750px;height:16px;
    background:linear-gradient(90deg,var(--gold-deep),var(--gold) 30%,var(--gold) 70%,var(--gold-deep));
    color:var(--ink);text-align:center;font-family:"EB Garamond",serif;font-weight:700;font-size:11px;line-height:16px;
  }
  .flyer--back .contact-bar{top:758px}
  .contact-row{
    position:absolute;left:0;right:0;top:782px;height:22px;display:flex;justify-content:center;align-items:center;
    font-family:"EB Garamond",serif;font-size:9.6px;
  }
  .flyer--back .contact-row{top:790px}
  .contact-row span{padding:0 12px}
  .contact-row span + span{border-left:1.5px solid var(--white)}
  .label{
    position:absolute;top:888px;font-family:"EB Garamond",serif;font-weight:700;font-size:33px;color:var(--ink);
  }
  .label--front{left:310px}
  .label--back{left:796px;top:884px}
</style>
</head>
<body>
<div class="stage">

  <!-- FRONT -->
  <section class="flyer flyer--front">
    <svg class="hero" viewBox="0 0 405 262">
      <defs>
        <linearGradient id="photoFront" x1="0" y1="0" x2="1" y2="1">
          <stop offset="0" stop-color="#e8b89a"/>
          <stop offset=".45" stop-color="#f3dcc4"/>
          <stop offset=".7" stop-color="#5b7fa8"/>
          <stop offset="1" stop-color="#3a3a3a"/>
        </linearGradient>
      </defs>
      <rect width="405" height="262" fill="url(#photoFront)" role="img" aria-label="Photo of a tradesman applying window film to a sunlit glass roof"/>
      <path d="M0,258 L150,258 C240,256 300,222 405,196 L405,262 L0,262 Z" fill="#f2cd1a"/>
      <path d="M0,262 L0,257 L150,257 C240,256 300,230 405,206 L405,262 Z" fill="#161618"/>
    </svg>
    <div class="brand"><span class="brand__name">BRIGHTLINE<br>WINDOW TINTING</span></div>

    <h1 class="headline headline--gold">KEEP HEAT OUT</h1>
    <p class="headline headline--white">BLOCK 99.9% UV RAYS</p>
    <div class="ribbon">
      <svg viewBox="0 0 336 72" preserveAspectRatio="none">
        <defs>
          <linearGradient id="ribbonFront" x1="0" x2="1">
            <stop offset="0" stop-color="#c99a0a"/><stop offset=".3" stop-color="#f2cd1a"/>
            <stop offset=".6" stop-color="#fbe45c"/><stop offset="1" stop-color="#c99a0a"/>
          </linearGradient>
        </defs>
        <path d="M14,0 Q170,10 336,0 L318,36 L336,72 Q170,62 0,72 L22,36 Z" fill="url(#ribbonFront)"/>
      </svg>
      <span class="ribbon__text">SAVE MONEY</span>
    </div>
    <p class="headline headline--privacy">INCREASE PRIVACY</p>

    <p class="benefits">Reduce glare. Reduce energy costs. Control the amount of light entering your home. Reduce carbon footprint. Make home more beautiful. Eliminate home hot spots. Protect against broken glass. Regulate energy. Protects upholstery. Improve effectiveness of roof insulation. Improve health. Reduces interior floor fading. Eliminate need for blinds. Strengthen your windows. Insulate in winter. Affordable</p>

    <div class="reasons">20 REASONS WHY<br>HOME WINDOW TINTING<br>IS PERFECT FOR YOU</div>

    <div class="cta">
      <p class="cta__text">CALL BRISBANE’S LEADER IN<br>HOME WINDOW TINTING NOW.</p>
      <div class="cta__icon">
        <svg width="30" height="48" viewBox="0 0 30 48"><rect x="2" y="2" width="26" height="44" rx="3" fill="none" stroke="#0d0d0f" stroke-width="3.5"/><rect x="2" y="38" width="26" height="8" fill="#0d0d0f"/></svg>
      </div>
    </div>

    <div class="contact-bar">Contact Us</div>
    <div class="contact-row">
      <span>TEL: 07 3000 1234</span><span>SMS: 0400 000 111</span><span>www.brightlinetinting.com.au</span>
    </div>
  </section>

  <!-- BACK -->
  <section class="flyer flyer--back">
    <svg class="hero" viewBox="0 0 405 262">
      <defs>
        <linearGradient id="photoBack" x1="0" y1="0" x2="1" y2="0">
          <stop offset="0" stop-color="#d8d8d4"/>
          <stop offset=".45" stop-color="#4a5f9a"/>
          <stop offset=".75" stop-color="#9fc3d8"/>
          <stop offset="1" stop-color="#7f9a5a"/>
        </linearGradient>
      </defs>
      <rect width="405" height="262" fill="url(#photoBack)" role="img" aria-label="Photo of a young tradesman sealing a window frame with trees outside"/>
      <path d="M0,206 C30,170 90,160 140,185 C190,210 220,245 260,247 L405,246 L405,262 L0,262 Z" fill="#f2cd1a"/>
      <path d="M0,214 C40,182 95,178 140,198 C190,222 220,252 262,254 L405,252 L405,262 L0,262 Z" fill="#161618"/>
    </svg>
    <div class="brand"><span class="brand__name">BRIGHTLINE<br>WINDOW TINTING</span></div>

    <h2 class="headline headline--gold">KEEP HEAT OUT</h2>
    <p class="headline headline--white">BLOCK 99.9% UV RAYS</p>
    <div class="ribbon">
      <svg viewBox="0 0 336 72" preserveAspectRatio="none">
        <defs>
          <linearGradient id="ribbonBack" x1="0" x2="1">
            <stop offset="0" stop-color="#c99a0a"/><stop offset=".3" stop-color="#f2cd1a"/>
            <stop offset=".6" stop-color="#fbe45c"/><stop offset="1" stop-color="#c99a0a"/>
          </linearGradient>
        </defs>
        <path d="M14,0 Q170,10 336,0 L318,36 L336,72 Q170,62 0,72 L22,36 Z" fill="url(#ribbonBack)"/>
      </svg>
      <span class="ribbon__text">SAVE MONEY</span>
    </div>
    <p class="headline headline--privacy">INCREASE PRIVACY</p>

    <p class="benefits">Reduce glare. Reduce energy costs. Control the amount of light entering your home. Reduce carbon footprint. Make home more beautiful. Eliminate home hot spots. Protect against broken glass. Regulate energy. Protects upholstery. Improve effectiveness of roof insulation. Improve health. Reduces interior floor fading. Eliminate need for blinds. Strengthen your windows. Insulate in winter. Affordable</p>

    <div class="reasons">20 REASONS WHY<br>HOME WINDOW TINTING<br>IS PERFECT FOR YOU</div>

    <div class="cta">
      <p class="cta__text">CALL BRISBANE’S LEADER IN<br>HOME WINDOW TINTING NOW.</p>
      <div class="cta__icon">
        <svg width="30" height="48" viewBox="0 0 30 48"><rect x="2" y="2" width="26" height="44" rx="3" fill="none" stroke="#0d0d0f" stroke-width="3.5"/><rect x="2" y="38" width="26" height="8" fill="#0d0d0f"/></svg>
      </div>
    </div>

    <div class="contact-bar">Contact Us</div>
    <div class="contact-row">
      <span>TEL: 07 3000 1234</span><span>SMS: 0400 000 111</span><span>www.brightlinetinting.com.au</span>
    </div>
  </section>

  <p class="label label--front">Front</p>
  <p class="label label--back">Back</p>
</div>
</body>
</html>
```